Graduation backdrop sign

I need a sign that says
Hey look ma...we made it!.
I want the Hey look ma on one line and in a more blocky font and then the other line of we made it in a more feminine font but something you can read. I am planning to send this file to a printing place to make an acrylic sign. The backdrop color is a bright pink, fuscia and orange colors with gold accent so I am thinking of the background being white with a cute scallop border or a cloud like border. Then make the colors of the fonts be a bright dark pink with orange and gold accents somehow. and maybe a cute but no overwhelming border or accents around the font to make it bright and cheery. I am attaching the backdrop that this will be hung in.

```html
<!DOCTYPE html>
<html lang="en">
<head>
<meta charset="UTF-8">
<title>Hey Look Ma… We Made It! — Graduation Backdrop Sign</title>
<link rel="stylesheet" href="https://fonts.googleapis.com/css2?family=Luckiest+Guy&family=Dancing+Script:wght@500&display=swap">
<style>
  :root {
    --page-bg: #e2dfde;
    --sign-white: #ffffff;
    --fuchsia: #c8157f;
    --rose: #e0566f;
    --orange: #f5913a;
    --gold-deep: #c48a25;
    --gold-light: #f6e268;
    --gold-mid: #d9a63a;
  }
  html, body {
    margin: 0;
    padding: 0;
    width: 1200px;
    height: 960px;
    overflow: hidden;
    background: var(--page-bg);
  }
  .canvas {
    position: relative;
    width: 1200px;
    height: 960px;
  }
  .sign-shape {
    position: absolute;
    left: 0;
    top: 0;
    filter: drop-shadow(14px 16px 14px rgba(0,0,0,0.22));
  }
  .headline {
    position: absolute;
    left: 0;
    width: 1200px;
    margin: 0;
    text-align: center;
    white-space: nowrap;
    background-clip: text;
    -webkit-background-clip: text;
    color: transparent;
    -webkit-text-fill-color: transparent;
  }
  .headline--block {
    top: 300px;
    padding-left: 84px;
    box-sizing: border-box;
    font-family: "Luckiest Guy", "Arial Black", Impact, sans-serif;
    font-size: 104px;
    line-height: 1;
    font-weight: 900;
    text-transform: uppercase;
    letter-spacing: -2px;
    transform: scale(0.9, 1.32);
    transform-origin: 642px 0;
    background-image: linear-gradient(90deg, var(--fuchsia) 15%, var(--orange) 32%, var(--fuchsia) 42%, var(--rose) 60%, var(--orange) 80%, var(--fuchsia) 96%);
  }
  .headline--script {
    top: 462px;
    font-family: "Dancing Script", cursive;
    font-size: 190px;
    line-height: 1;
    font-weight: 500;
    background-image: linear-gradient(90deg, var(--gold-deep) 24%, var(--gold-light) 52%, var(--gold-mid) 76%);
  }
  .flourish {
    position: absolute;
    left: 404px;
    top: 660px;
    width: 392px;
    height: 40px;
    border-radius: 20px;
    background: linear-gradient(90deg, var(--orange), var(--fuchsia) 50%, var(--orange));
    opacity: 0.5;
  }
</style>
</head>
<body>
<div class="canvas">
  <svg class="sign-shape" width="1200" height="960" viewBox="0 0 1200 960">
    <defs>
      <linearGradient id="border-gradient" x1="83" y1="0" x2="1119" y2="0" gradientUnits="userSpaceOnUse">
        <stop offset="0" stop-color="#c8157f"/>
        <stop offset="0.5" stop-color="#e4666b"/>
        <stop offset="1" stop-color="#f5913a"/>
      </linearGradient>
      <radialGradient id="floral-tint">
        <stop offset="0" stop-color="#f3e6cf"/>
        <stop offset="0.6" stop-color="#f3e6cf" stop-opacity="0.35"/>
        <stop offset="1" stop-color="#ffffff" stop-opacity="0"/>
      </radialGradient>
      <clipPath id="plaque-inside">
        <path d="M 153 223 H 1049 A 70 70 0 0 0 1119 293 V 665 A 70 70 0 0 0 1049 735 H 153 A 70 70 0 0 0 83 665 V 293 A 70 70 0 0 0 153 223 Z"/>
      </clipPath>
    </defs>
    <path class="sign-plaque"
      d="M 153 223 H 1049 A 70 70 0 0 0 1119 293 V 665 A 70 70 0 0 0 1049 735 H 153 A 70 70 0 0 0 83 665 V 293 A 70 70 0 0 0 153 223 Z"
      fill="#ffffff"/>
    <g clip-path="url(#plaque-inside)">
      <ellipse class="floral-corner" cx="200" cy="555" rx="95" ry="140" fill="url(#floral-tint)" role="img" aria-label="Fine gold line-drawn lilies and buds in the lower left corner"/>
      <ellipse class="floral-corner" cx="1005" cy="575" rx="85" ry="130" fill="url(#floral-tint)" role="img" aria-label="Fine gold line-drawn lilies and buds in the right corner"/>
    </g>
    <path class="sign-border"
      d="M 153 223 H 1049 A 70 70 0 0 0 1119 293 V 665 A 70 70 0 0 0 1049 735 H 153 A 70 70 0 0 0 83 665 V 293 A 70 70 0 0 0 153 223 Z"
      fill="none" stroke="url(#border-gradient)" stroke-width="18" stroke-linejoin="round"/>
  </svg>

  <h1 class="headline headline--block">Hey Look Ma...</h1>
  <p class="headline headline--script">We made it!</p>

  <div class="flourish" role="img" aria-label="Pink and orange scroll flourish ornament"></div>
</div>
</body>
</html>
```